Consulting Group Needs a Graphic Design

We have created a unique, cyclical process to describe our company's philosophy on parenting to our clients. It is provided in the attached file. At the center of the graphic design, which includes all written words on the page, is an image of a gardener that we really like. We found it through a clipart service, but we are not able to trademark it as our own. We would like to create a similar image which includes the female gardener tending the garden, with a trowel in her hand and a watering can at her side. We want the flowers in her garden to be different, just as every child is unique and different within the same family. For more perspective on our company, please visit www.brookhavenfamilyway.com.
Updates

Project Deadline Extended
Reason: Some of the designers are getting very close to what we want. Due to some unforeseen circumstances, we were unable to give feedback for a couple of days. We would really appreciate your consideration of our request. We are eager to get the design finished to move forward with our branding strategy, so we will be hyper-focused on the project over the coming days. Thank you, Tillmore Family Consultants

Project Deadline Extended
Reason: We would like to give our first choice designer a chance to create a complementary logo to accompany his submission. We have been in communication with this designer.

Industry/Entity Type

Gardener

```html
<!DOCTYPE html>
<html lang="en">
<head>
<meta charset="utf-8">
<title>Every Good Gardener</title>
<link href="https://fonts.googleapis.com/css2?family=Chewy&family=Short+Stack&display=swap" rel="stylesheet">
<style>
  :root {
    --green-deep: #0b8a45;
    --green-mid: #1fa84a;
    --green-ray: #34b64f;
    --lime: #c9e534;
    --sun: #e6ef2a;
    --oval-dark: #06743a;
    --oval-light: #2bb35a;
    --banner: #b7dc3a;
    --ink-dark: #0b4d22;
    --white: #ffffff;
  }
  html, body {
    margin: 0;
    padding: 0;
    width: 1200px;
    height: 922px;
    overflow: hidden;
    background: #f2f2f2;
  }
  .poster {
    position: relative;
    width: 1200px;
    height: 922px;
    overflow: hidden;
    background:
      radial-gradient(ellipse 520px 380px at 600px 110px, rgba(230,239,42,0.95) 0%, rgba(180,225,50,0.6) 35%, rgba(52,182,79,0) 75%),
      repeating-conic-gradient(from 0deg at 600px 110px, var(--green-ray) 0deg 7deg, var(--green-mid) 7deg 14deg),
      var(--green-deep);
  }
  .poster::after {
    content: "";
    position: absolute;
    inset: 0;
    background: radial-gradient(ellipse 900px 700px at 600px 300px, rgba(0,0,0,0) 40%, rgba(6,110,55,0.55) 100%);
    pointer-events: none;
  }
  .title {
    position: absolute;
    top: 30px;
    left: 0;
    width: 100%;
    margin: 0;
    text-align: center;
    font-family: "Chewy", cursive;
    font-weight: 400;
    font-size: 74px;
    letter-spacing: 1px;
    color: var(--white);
    text-shadow: 3px 4px 0 #1d3a10, 4px 6px 6px rgba(0,0,0,0.35);
    z-index: 2;
  }
  .cycle {
    position: absolute;
    inset: 0;
    z-index: 1;
  }
  .cycle-line {
    fill: none;
    stroke: var(--white);
    stroke-width: 3;
  }
  .arrowhead {
    fill: none;
    stroke: var(--white);
    stroke-width: 3;
    stroke-linecap: round;
    stroke-linejoin: round;
  }
  .step-oval {
    fill: url(#ovalFill);
    stroke: var(--white);
    stroke-width: 3;
  }
  .step-label {
    font-family: "Short Stack", cursive;
    font-size: 27px;
    fill: var(--white);
    text-anchor: middle;
  }
  .garden-scene {
    fill: url(#sceneFill);
  }
  .banner {
    fill: none;
    stroke: var(--banner);
    stroke-width: 44;
    stroke-linecap: round;
  }
  .motto {
    font-family: "Short Stack", cursive;
    font-size: 19px;
    fill: var(--ink-dark);
  }
  .credit {
    position: absolute;
    left: 361px;
    top: 839px;
    width: 479px;
    height: 36px;
    border-radius: 18px;
    background: var(--banner);
    color: var(--ink-dark);
    font-family: "Short Stack", cursive;
    font-size: 18px;
    line-height: 36px;
    text-align: center;
    z-index: 2;
  }
</style>
</head>
<body>
<main class="poster">
  <h1 class="title">Every Good Gardener:</h1>

  <svg class="cycle" width="1200" height="922" viewBox="0 0 1200 922">
    <defs>
      <radialGradient id="ovalFill" cx="50%" cy="45%" r="60%">
        <stop offset="0%" stop-color="var(--oval-light)"/>
        <stop offset="100%" stop-color="var(--oval-dark)"/>
      </radialGradient>
      <radialGradient id="sceneFill" cx="50%" cy="55%" r="55%">
        <stop offset="0%" stop-color="#7cc94a"/>
        <stop offset="60%" stop-color="#4fb446" stop-opacity="0.85"/>
        <stop offset="100%" stop-color="#3aa846" stop-opacity="0"/>
      </radialGradient>
      <path id="mottoPath" d="M330,700 C420,712 480,700 560,672 C640,644 760,640 860,632"/>
    </defs>

    <!-- cycle loop -->
    <ellipse class="cycle-line" cx="598" cy="500" rx="445" ry="295"/>

    <!-- arrowheads -->
    <polyline class="arrowhead" points="840,270 868,296 836,312"/>
    <polyline class="arrowhead" points="1020,500 1042,530 1066,500"/>
    <polyline class="arrowhead" points="608,772 580,795 608,818"/>
    <polyline class="arrowhead" points="133,550 157,522 180,550"/>
    <polyline class="arrowhead" points="344,292 368,250 390,268"/>
    <polyline class="arrowhead" points="462,208 482,218 466,238"/>

    <!-- central garden illustration area -->
    <ellipse class="garden-scene" cx="594" cy="480" rx="300" ry="200" role="img" aria-label="Illustration of a girl gardener with a watering can and trowel tending a hillside of varied flowers with trees and butterflies"/>

    <!-- motto ribbon -->
    <path class="banner" d="M330,690 C420,702 480,690 560,662 C640,634 760,630 880,622"/>
    <text class="motto"><textPath href="#mottoPath" startOffset="40">“Growing strong families every day!”</textPath></text>

    <!-- cycle steps -->
    <g class="step">
      <ellipse class="step-oval" cx="600" cy="211" rx="112" ry="63"/>
      <text class="step-label" x="600" y="204">Plants with</text>
      <text class="step-label" x="600" y="238">purpose</text>
    </g>
    <g class="step">
      <ellipse class="step-oval" cx="1004" cy="346" rx="112" ry="63"/>
      <text class="step-label" x="1004" y="356">Nurtures</text>
    </g>
    <g class="step">
      <ellipse class="step-oval" cx="957" cy="684" rx="112" ry="63"/>
      <text class="step-label" x="957" y="676">Enriches</text>
      <text class="step-label" x="957" y="710">the soil</text>
    </g>
    <g class="step">
      <ellipse class="step-oval" cx="253" cy="684" rx="112" ry="63"/>
      <text class="step-label" x="253" y="678">Prunes as</text>
      <text class="step-label" x="253" y="712">needed</text>
    </g>
    <g class="step">
      <ellipse class="step-oval" cx="200" cy="346" rx="112" ry="63"/>
      <text class="step-label" x="200" y="338">Measures</text>
      <text class="step-label" x="200" y="372">growth</text>
    </g>
  </svg>

  <p class="credit">© 2009 Tillmore Family Consultants</p>
</main>
</body>
</html>
```